Website Landing Page for Brightfall Systems

Create a custom designed website landing page for our business. Looking for a professional upscale design that incorporates our logo and logo colors into the theme. I want a standard fixed frame website, not a constant scrolling format that seems to be the trend. To start with I'm looking for more of the graphic design part, maybe a concept or theme, I don't expect to see a finished project. Not interested in generic templates or layouts.

The name of our company is Brightfall Systems and I've attached our logo below. I'd like to have the web page have the same look and feel of our logo, as well as the colors. Our company, Brightfall Systems does system design, installation, and programming, of residential and commercial Audio/Video and Automation systems. We do home theaters, lighting and building automation, video conferencing systems, security camera installations, conference rooms, projectors, distributed audio systems, and similar Technology projects. This will be a professional services/informational website. We will not sell products on this website. This website will be used to advertise our company and communicate our services to prospective customers. Having a well designed, professional and clean website is one way we want to distinguish our company from the competition.

Here are some examples of what I consider a professional well designed website
http://www.qorlamstudio.com/Work/

Last year we had our tradlo store designed (with PixelMarket) and I'm really happy with the way it turned out. You can see it at www.HolvenGearDepot.com I consider this to be a great design and looking for the same level of quality with this new website. However, do not copy or use any part of this design in this new project. This tradlo store is completely separate from our other company Brightfall Systems. I only mention this tradlo store an an example of good work.

Reason: Still going through designs.

Reason: Still working on project and have not had time to review all designs and request revisions.

Reason: Sill going through designs and requesting revisions

Reason: still going through all the submissions we received.

Target Market(s)

People interested in Audio/Video, home theaters, home automation. We do sales, system design, and programming. We typically work on larger projects with both residential and commercial customers.

Industry/Entity Type

Business

Number of Pages Required

1 page

Requirements
Must have
• Great design elements. Please use a white background. I think white goes well with our logo colors.

```html
<!DOCTYPE html>
<html lang="en">
<head>
<meta charset="utf-8">
<title>Brightfall Systems</title>
<link href="https://fonts.googleapis.com/css2?family=Montserrat:wght@300;400;500;600&display=swap" rel="stylesheet">
<style>
:root{
  --blue:#3a86c8;
  --blue-dark:#2b6fae;
  --green:#7dc242;
  --ink:#333538;
  --muted:#6d6f73;
  --dark-bar:#1f2023;
  --grey-band:#ececec;
  --white:#ffffff;
  --line:#d6d6d6;
}
*{box-sizing:border-box;margin:0;padding:0}
html,body{width:1200px;height:3830px;overflow:hidden}
body{position:relative;background:var(--white);font-family:'Montserrat',sans-serif;color:var(--ink)}
.abs{position:absolute}
h2,h3,h4{font-weight:400}

/* header */
.topbar{left:0;top:0;width:1200px;height:38px}
.topbar-info{top:10px;font-size:13px;color:var(--white);display:flex;align-items:center;gap:8px}
.topbar-info svg{width:13px;height:13px}
.brand{left:97px;top:22px;display:flex;align-items:center;gap:14px}
.brand-dot{width:52px;height:52px;border-radius:50%;background:var(--blue)}
.brand-name{font-size:24px;font-weight:600;color:var(--blue);line-height:1.05;letter-spacing:.5px;text-transform:uppercase}
.main-nav{top:74px;left:443px;display:flex;gap:0}
.main-nav a{font-size:13px;color:var(--ink);text-decoration:none;letter-spacing:.5px;margin-right:40px}
.quote-btn{left:957px;top:66px;width:146px;height:34px;border-radius:17px;background:var(--blue);color:var(--white);font-size:12px;font-weight:500;letter-spacing:.5px;display:flex;align-items:center;justify-content:center}

/* hero */
.hero-photo{left:0;top:123px;width:1200px;height:560px;background:linear-gradient(180deg,#6d5c4d 0%,#8a7563 35%,#a48c75 55%,#5a4536 80%,#3e2f25 100%)}
.hero-shade{left:0;top:123px;width:700px;height:560px;background:linear-gradient(90deg,rgba(30,22,16,.55),rgba(30,22,16,0))}
.hero-wave{left:0;top:610px;width:1200px;height:80px}
.hero-kicker{left:94px;top:293px;font-size:22px;font-weight:300;color:var(--white)}
.hero-title{left:94px;top:330px;font-size:46px;font-weight:500;color:var(--white);letter-spacing:1px}
.hero-sub{left:94px;top:398px;font-size:21px;font-weight:300;color:var(--white)}
.btn{top:465px;width:149px;height:40px;font-size:13px;display:flex;align-items:center;justify-content:center}
.btn-ghost{left:94px;border:1px solid var(--white);color:var(--white)}
.btn-solid{left:268px;background:var(--white);color:var(--ink)}

/* about */
.about-title{left:97px;top:853px;font-size:33px;font-weight:400;line-height:1.3;color:var(--ink)}
.about-title b{font-weight:500;color:var(--blue)}
.about-text{left:97px;top:955px;width:400px;font-size:12.5px;line-height:1.7;color:var(--muted)}
.about-photos{left:610px;top:780px;width:410px;height:410px}

/* section headings */
.section-title{left:0;width:1200px;text-align:center;font-size:33px;font-weight:400;color:var(--ink)}
.section-title b{font-weight:500;color:var(--blue)}

/* services */
.services-band{left:0;top:1320px;width:1200px;height:900px}
.service-card{width:319px;height:233px;background:var(--white);box-shadow:0 2px 8px rgba(0,0,0,.08);text-align:center}
.service-icon{position:absolute;left:50%;top:-28px;width:50px;height:56px;margin-left:-25px}
.service-card h3{margin-top:70px;font-size:14px;font-weight:500;color:var(--blue)}
.service-card p{margin:28px 28px 0;text-align:left;font-size:12px;line-height:1.7;color:var(--muted)}

/* products */
.product-tabs{left:0;top:2346px;width:1200px;display:flex;justify-content:center;gap:32px}
.product-tabs span{font-size:12px;letter-spacing:.6px;color:var(--muted);padding:6px 10px;border:1px solid transparent}
.product-tabs .active{color:var(--blue);border-color:var(--blue)}
.product-photo{left:0;top:2425px;width:590px;height:511px;background:linear-gradient(160deg,#1e2124 0%,#5a5048 40%,#c9a57a 70%,#7c6650 100%)}
.product-title{left:625px;top:2455px;font-size:33px;line-height:1.3;color:var(--ink);font-weight:400}
.product-title b{font-weight:500;color:var(--blue)}
.product-text{left:628px;top:2555px;width:420px;font-size:12.5px;line-height:1.7;color:var(--muted)}
.product-text p+p{margin-top:22px}

/* contact */
.contact-band{left:590px;top:3040px;width:610px;height:530px}
.contact-photo{left:0;top:3076px;width:590px;height:442px;background:linear-gradient(180deg,#cfc6b9 0%,#b9a893 40%,#6b4e37 70%,#8d8072 100%)}
.contact-title{left:590px;top:3090px;width:610px;text-align:center;font-size:33px;font-weight:400;color:var(--ink)}
.contact-title b{font-weight:500;color:var(--blue)}
.contact-intro{left:625px;top:3150px;width:470px;text-align:center;font-size:12.5px;line-height:1.7;color:var(--ink)}
.field{background:var(--white);font-size:12px;color:#9a9a9a;padding:14px 14px}

/* footer */
.footer-brand{left:97px;top:3605px;width:160px;text-align:center}
.footer-brand .brand-dot{width:70px;height:70px;margin:0 auto 10px}
.footer-brand span{font-size:13px;font-weight:600;color:var(--blue);letter-spacing:.5px;text-transform:uppercase}
.footer-address{left:97px;top:3740px;font-size:12.5px;line-height:1.7;color:var(--muted);font-style:normal}
.footer-col{top:3606px;width:200px}
.footer-col h4{font-size:17px;font-weight:500;color:var(--ink);padding-bottom:12px;border-bottom:1px solid var(--line);width:170px}
.footer-col a{display:block;margin-top:22px;font-size:13px;color:var(--muted);text-decoration:none}
</style>
</head>
<body>

<!-- header -->
<svg class="abs topbar" viewBox="0 0 1200 38" aria-hidden="true"><polygon points="408,0 1200,0 1200,38 448,38" fill="#1f2023"/></svg>
<div class="abs topbar-info" style="left:443px">
  <svg viewBox="0 0 16 16"><path d="M3 1l3 3-2 2c1 2 3 4 5 5l2-2 3 3-2 3C6 15 1 10 1 3z" fill="#fff"/></svg>
  Call us: 61 3 5550 1947
</div>
<div class="abs topbar-info" style="left:700px">
  <svg viewBox="0 0 16 16"><rect x="1" y="3" width="14" height="10" fill="#fff"/><path d="M1 3l7 6 7-6" stroke="#1f2023" fill="none"/></svg>
  Email: help24-7@brightfallsys.com
</div>

<div class="abs brand"><div class="brand-dot"></div><div class="brand-name">Brightfall<br>Systems</div></div>
<nav class="abs main-nav"><a>HOME</a><a>ABOUT</a><a>PRODUCTS</a><a>SERVICES</a><a>CONTACT</a></nav>
<div class="abs quote-btn">GET A QUOTE</div>

<!-- hero -->
<div class="abs hero-photo" role="img" aria-label="Photo of a modern living room with a wall-mounted screen and media console"></div>
<div class="abs hero-shade"></div>
<svg class="abs hero-wave" viewBox="0 0 1200 80" preserveAspectRatio="none" aria-hidden="true"><path d="M0,30 C300,70 700,80 1200,10 L1200,80 L0,80 Z" fill="#fff"/></svg>
<div class="abs hero-kicker">Clean Layered Source File</div>
<div class="abs hero-title">EASY TO CUSTOMIZE</div>
<div class="abs hero-sub">We deliver best quality products and services</div>
<div class="abs btn btn-ghost">View more</div>
<div class="abs btn btn-solid">Download</div>

<!-- about -->
<h2 class="abs about-title">A <b>Professional</b> &amp; Hard<br>Working Team</h2>
<p class="abs about-text">We design, install and program audio, video and automation systems for homes and businesses across the region. Our engineers plan every project from the first walkthrough to the final handover, so each room works the way you expect. From quiet home theaters to busy conference rooms, we build clean, reliable systems that are easy to use every single day and simple to extend as your needs grow over time with our team.</p>
<svg class="abs about-photos" viewBox="0 0 410 410" role="img" aria-label="Four diamond-shaped photos of office towers and modern interiors">
  <defs>
    <linearGradient id="gTop" x1="0" y1="0" x2="1" y2="1"><stop offset="0" stop-color="#2d56a6"/><stop offset="1" stop-color="#c9d3e4"/></linearGradient>
    <linearGradient id="gLeft" x1="0" y1="0" x2="1" y2="1"><stop offset="0" stop-color="#e7dcc8"/><stop offset="1" stop-color="#8a6a4a"/></linearGradient>
    <linearGradient id="gRight" x1="0" y1="0" x2="1" y2="1"><stop offset="0" stop-color="#d9cdb5"/><stop offset="1" stop-color="#5f7c3e"/></linearGradient>
    <linearGradient id="gBottom" x1="0" y1="0" x2="1" y2="1"><stop offset="0" stop-color="#f2f2f2"/><stop offset="1" stop-color="#9aa1a8"/></linearGradient>
  </defs>
  <polygon points="202,10 300,98 202,186 104,98" fill="url(#gTop)"/>
  <polygon points="105,104 203,192 105,280 7,192" fill="url(#gLeft)"/>
  <polygon points="304,104 402,192 304,280 206,192" fill="url(#gRight)"/>
  <polygon points="202,198 300,286 202,374 104,286" fill="url(#gBottom)"/>
</svg>

<!-- services -->
<svg class="abs services-band" viewBox="0 0 1200 900" preserveAspectRatio="none" aria-hidden="true">
  <path d="M0,20 C350,-10 800,60 1200,10 L1200,850 C800,880 400,820 0,870 Z" fill="#ececec"/>
</svg>
<h2 class="abs section-title" style="top:1400px">Our <b>Services</b></h2>

<div class="abs service-card" style="left:97px;top:1534px"><svg class="service-icon" viewBox="0 0 50 56"><path d="M25 2a4 4 0 0 1 4 4v2c9 2 13 10 13 20v10l6 8H2l6-8V28C8 18 12 10 21 8V6a4 4 0 0 1 4-4z" fill="#3a86c8"/><circle cx="25" cy="51" r="5" fill="#3a86c8"/></svg><h3>Installation and maintenance</h3><p>We set up and service your equipment, keeping every system running smoothly all year.</p></div>
<div class="abs service-card" style="left:440px;top:1534px"><svg class="service-icon" viewBox="0 0 50 56"><path d="M25 2a4 4 0 0 1 4 4v2c9 2 13 10 13 20v10l6 8H2l6-8V28C8 18 12 10 21 8V6a4 4 0 0 1 4-4z" fill="#3a86c8"/><circle cx="25" cy="51" r="5" fill="#3a86c8"/></svg><h3>Installation and maintenance</h3><p>We set up and service your equipment, keeping every system running smoothly all year.</p></div>
<div class="abs service-card" style="left:784px;top:1534px"><svg class="service-icon" viewBox="0 0 50 56"><path d="M25 2a4 4 0 0 1 4 4v2c9 2 13 10 13 20v10l6 8H2l6-8V28C8 18 12 10 21 8V6a4 4 0 0 1 4-4z" fill="#3a86c8"/><circle cx="25" cy="51" r="5" fill="#3a86c8"/></svg><h3>Installation and maintenance</h3><p>We set up and service your equipment, keeping every system running smoothly all year.</p></div>
<div class="abs service-card" style="left:97px;top:1836px"><svg class="service-icon" viewBox="0 0 50 56"><path d="M25 2a4 4 0 0 1 4 4v2c9 2 13 10 13 20v10l6 8H2l6-8V28C8 18 12 10 21 8V6a4 4 0 0 1 4-4z" fill="#3a86c8"/><circle cx="25" cy="51" r="5" fill="#3a86c8"/></svg><h3>Installation and maintenance</h3><p>We set up and service your equipment, keeping every system running smoothly all year.</p></div>
<div class="abs service-card" style="left:440px;top:1836px"><svg class="service-icon" viewBox="0 0 50 56"><path d="M25 2a4 4 0 0 1 4 4v2c9 2 13 10 13 20v10l6 8H2l6-8V28C8 18 12 10 21 8V6a4 4 0 0 1 4-4z" fill="#3a86c8"/><circle cx="25" cy="51" r="5" fill="#3a86c8"/></svg><h3>Installation and maintenance</h3><p>We set up and service your equipment, keeping every system running smoothly all year.</p></div>
<div class="abs service-card" style="left:784px;top:1836px"><svg class="service-icon" viewBox="0 0 50 56"><path d="M25 2a4 4 0 0 1 4 4v2c9 2 13 10 13 20v10l6 8H2l6-8V28C8 18 12 10 21 8V6a4 4 0 0 1 4-4z" fill="#3a86c8"/><circle cx="25" cy="51" r="5" fill="#3a86c8"/></svg><h3>Installation and maintenance</h3><p>We set up and service your equipment, keeping every system running smoothly all year.</p></div>

<!-- products -->
<h2 class="abs section-title" style="top:2268px">Our <b>Products</b></h2>
<div class="abs product-tabs"><span class="active">AUTOMATION SYSTEMS</span><span>VIDEO CONFERENCING</span><span>SECURITY CAMERAS</span><span>PROJECTORS</span><span>AUDIO SYSTEMS</span></div>
<div class="abs product-photo" role="img" aria-label="Photo of a modern bar interior with tall stools and pendant lights"></div>
<h3 class="abs product-title"><b>Automation systems</b><br>installation</h3>
<div class="abs product-text">
  <p>Our automation systems bring lighting, shades, climate and media together in one simple interface. We plan each installation around the way you live and work, then program scenes that respond at the touch of a button, from a wall keypad, a phone or a tablet anywhere in the building.</p>
  <p>Every system is tested on site before handover, and our team stays on call for updates, tuning and support. As your space changes, we can add rooms, devices and new features without replacing the equipment you already own, keeping the whole setup tidy and easy to manage.</p>
</div>

<!-- contact -->
<svg class="abs contact-band" viewBox="0 0 610 530" preserveAspectRatio="none" aria-hidden="true">
  <path d="M0,30 C250,40 450,0 610,20 L610,500 C450,520 250,470 0,480 Z" fill="#ececec"/>
</svg>
<div class="abs contact-photo" role="img" aria-label="Photo of a bright living room with a wall-mounted screen and speakers"></div>
<h2 class="abs contact-title">Get <b>in touch</b></h2>
<p class="abs contact-intro">Please use contact form below to send your inquiries, questions, queries or request for quotation. We are available 24x7 to answer your emails.</p>
<div class="abs field" style="left:613px;top:3224px;width:235px;height:46px">Your Name</div>
<div class="abs field" style="left:868px;top:3224px;width:237px;height:46px">Email</div>
<div class="abs field" style="left:613px;top:3288px;width:492px;height:46px">Subject</div>
<div class="abs field" style="left:613px;top:3352px;width:492px;height:146px">Message</div>

<!-- footer -->
<div class="abs footer-brand"><div class="brand-dot"></div><span>Brightfall Systems</span></div>
<address class="abs footer-address">4120 Po.Box Larkfield<br>Norren 31008</address>
<div class="abs footer-col" style="left:355px"><h4>Services</h4><a>Design service</a><a>Writing service</a><a>Dev service</a><a>Outside service</a></div>
<div class="abs footer-col" style="left:610px"><h4>Customers</h4><a>Design service</a><a>Writing service</a><a>Dev service</a></div>
<div class="abs footer-col" style="left:868px"><h4>Employers</h4><a>Design service</a><a>Writing service</a><a>Dev service</a><a>Outside service</a></div>

</body>
</html>
```